Business Card Design

Company is a Commercial Building Company specialising in New Construction and existing refurbishments

Business

Contact Information for Business Card

Derek Halloway
Construction Manager
E Derek@ridgemarkbuilding.com.au
M 0400 215 397
Mail 14 Tarrington Loop Dawesville WA 6211

```html
<!DOCTYPE html>
<html lang="en">
<head>
<meta charset="utf-8">
<title>Ridgemark Building &amp; Construction — Business Card</title>
<link rel="stylesheet" href="https://fonts.googleapis.com/css2?family=Saira:wght@400;500;700;800&display=swap">
<style>
  :root {
    --slate: #353a4e;
    --cyan: #00b5d8;
    --orange: #f28c1e;
    --white: #ffffff;
    --paper: #fbfbfb;
    --ink: #3b3f52;
    --page: #ffffff;
  }
  * { margin: 0; padding: 0; box-sizing: border-box; }
  html, body {
    width: 932px; height: 1200px; overflow: hidden;
    background: var(--page);
    font-family: "Saira", sans-serif;
  }
  .sheet { position: relative; width: 932px; height: 1200px; }
  .card {
    position: absolute; left: 75px; width: 768px; height: 455px;
    border-radius: 28px; overflow: hidden;
    box-shadow: 0 4px 14px rgba(0,0,0,0.28);
  }
  .card--front { top: 96px; background: var(--slate); }
  .card--back { top: 648px; background: var(--paper); }

  /* Front */
  .front-brand {
    position: absolute; left: 0; right: 0; top: 52px;
    display: flex; flex-direction: column; align-items: center;
  }
  .brand-square {
    width: 160px; height: 160px; background: var(--cyan); border-radius: 6px;
  }
  .front-name {
    margin-top: 34px; color: var(--white); text-align: center; line-height: 1.05;
    font-weight: 500;
  }
  .front-name__main { display: block; font-size: 48px; letter-spacing: 0.5px; }
  .front-name__sub { display: block; font-size: 45px; }

  /* Back */
  .back-top {
    position: absolute; left: 0; top: 0; width: 100%; height: 277px;
    background: var(--slate);
  }
  .back-rule {
    position: absolute; left: 0; top: 277px; width: 100%; height: 7px;
    background: var(--orange);
  }
  .back-brand {
    position: absolute; left: 48px; top: 58px;
    display: flex; align-items: center; gap: 12px;
  }
  .back-brand__square { width: 40px; height: 40px; background: var(--cyan); border-radius: 3px; }
  .back-brand__name { color: var(--white); font-size: 26px; font-weight: 500; letter-spacing: 0.5px; }
  .services {
    position: absolute; left: 287px; top: 50px; list-style: none;
    color: var(--white); font-weight: 800; font-size: 23px; letter-spacing: 0.6px;
    line-height: 42px;
  }
  .person { position: absolute; left: 288px; top: 200px; color: var(--white); }
  .person__name { font-size: 24px; font-weight: 800; letter-spacing: 0.4px; line-height: 30px; }
  .person__role { font-size: 22px; font-weight: 400; line-height: 30px; letter-spacing: 0.3px; }
  .contacts {
    position: absolute; left: 146px; top: 310px; list-style: none;
    color: var(--ink); font-size: 23px; letter-spacing: 0.3px; line-height: 33px;
  }
  .contacts li { display: flex; align-items: center; gap: 10px; }
  .contacts svg { width: 24px; height: 22px; flex: none; }
</style>
</head>
<body>
<main class="sheet">
  <section class="card card--front" aria-label="Card front">
    <div class="front-brand">
      <div class="brand-square" aria-hidden="true"></div>
      <h1 class="front-name">
        <span class="front-name__main">RIDGEMARK BUILDING</span>
        <span class="front-name__sub">&amp; CONSTRUCTION</span>
      </h1>
    </div>
  </section>

  <section class="card card--back" aria-label="Card back">
    <div class="back-top"></div>
    <div class="back-rule"></div>
    <div class="back-brand">
      <div class="back-brand__square" aria-hidden="true"></div>
      <span class="back-brand__name">RIDGEMARK</span>
    </div>
    <ul class="services">
      <li>NEW CONSTRUCTION</li>
      <li>AND</li>
      <li>EXISTING REFURBISHMENTS</li>
    </ul>
    <div class="person">
      <p class="person__name">Derek Halloway</p>
      <p class="person__role">Construction Manager</p>
    </div>
    <ul class="contacts">
      <li>
        <svg viewBox="0 0 24 22" aria-hidden="true"><rect x="2" y="5" width="20" height="13" fill="none" stroke="#f28c1e" stroke-width="2"/><path d="M2 5 L12 13 L22 5" fill="none" stroke="#f28c1e" stroke-width="2"/></svg>
        Derek@ridgemarkbuilding.com.au
      </li>
      <li>
        <svg viewBox="0 0 24 22" aria-hidden="true"><path d="M7 2 L10 7 L8 9 C9 12 11 14 14 15 L16 13 L20 16 L18 20 C11 20 4 13 4 5 Z" fill="#f28c1e"/></svg>
        0400 215 397
      </li>
      <li>
        <svg viewBox="0 0 24 22" aria-hidden="true"><path d="M1 9 L12 2 L23 9 Z" fill="#f28c1e"/><rect x="3" y="10" width="18" height="11" fill="#f28c1e"/><rect x="7" y="13" width="4" height="8" fill="#fbfbfb"/><rect x="13" y="13" width="4" height="4" fill="#fbfbfb"/></svg>
        14 Tarrington Loop Dawesville WA 6211
      </li>
    </ul>
  </section>
</main>
</body>
</html>
```